Meridel Capra SA Business Cards

Dear all,
Thank you for reading my brief and project. My company is doing doing advisory in real estate and to comapnies + real estates services as asset management, brokerage, development etc.
I would like to get a business card for my company which is clear, professionnal and serious.
Please have a look to the attachement to see the logos of the company

Industry/Entity Type

Real Estate

Contact Information for Business Card

I would like to have in the business card the following
Principal side:
- Logo of the company (or Monogram)
- First and Last Name (Paulo Vestrand)
- Mobile number
- email address

Second side:
- Address (Chemin des Orvets 17, 1226 Thônex - Switzerland)
- website (www.meridelcapra.ch)

Requirements
Must have
• Refer to the typeface and logo colors

```html
<!DOCTYPE html>
<html lang="en">
<head>
<meta charset="UTF-8">
<title>Meridel Capra SA – Business Cards</title>
<link href="https://fonts.googleapis.com/css2?family=Montserrat:wght@300;400;600&display=swap" rel="stylesheet">
<style>
  :root {
    --backdrop: #1c1d1f;
    --card-top: #4a586b;
    --card-bottom: #3b4858;
    --ink: #ffffff;
    --ink-soft: rgba(255,255,255,0.88);
    --accent: #2d8fd8;
    --ghost: rgba(255,255,255,0.06);
  }
  * { margin: 0; padding: 0; box-sizing: border-box; }
  html, body {
    width: 1200px; height: 1200px; overflow: hidden;
    background: var(--backdrop);
    font-family: "Montserrat", sans-serif;
    color: var(--ink);
  }
  .canvas { position: relative; width: 1200px; height: 1200px; }
  .card {
    position: absolute; left: 160px;
    width: 880px; height: 520px;
    border-radius: 30px;
    background: linear-gradient(160deg, var(--card-top), var(--card-bottom));
    overflow: hidden;
  }
  .card--front { top: 50px; }
  .card--back { top: 630px; }

  .ghost-circle {
    position: absolute; right: -60px; top: 60px;
    width: 380px; height: 380px; border-radius: 50%;
    background: var(--ghost);
  }

  .brand {
    display: flex; align-items: center; gap: 16px;
    position: absolute;
  }
  .brand__mark {
    width: 22px; height: 22px; background: var(--ink);
  }
  .brand__name {
    font-weight: 600; font-size: 28px; letter-spacing: 1.5px;
    text-transform: uppercase; color: var(--ink);
  }
  .card--front .brand { left: 50%; top: 205px; transform: translateX(-50%); }
  .card--front .website {
    position: absolute; left: 0; right: 0; bottom: 50px;
    text-align: center; font-size: 19px; letter-spacing: 1px;
    font-weight: 400; color: var(--ink-soft);
  }

  .card--back .brand { left: 80px; top: 245px; }
  .holder {
    position: absolute; right: 80px; top: 95px; text-align: right;
  }
  .holder__name {
    font-size: 28px; letter-spacing: 1.5px; text-transform: uppercase;
    margin-bottom: 18px;
  }
  .holder__first { font-weight: 600; }
  .holder__last { font-weight: 300; }
  .contact-list { list-style: none; }
  .contact-list li {
    display: flex; justify-content: flex-end; align-items: center; gap: 16px;
    font-size: 21px; font-weight: 400; line-height: 30px; letter-spacing: 0.5px;
  }
  .contact-list svg { width: 20px; height: 20px; fill: var(--accent); flex: none; }
  .rule {
    position: absolute; left: 480px; right: 80px; top: 330px;
    height: 2px; background: var(--ink);
  }
  .address {
    position: absolute; right: 80px; top: 355px;
    text-align: right; font-style: normal;
    font-size: 21px; line-height: 31px; letter-spacing: 0.6px; font-weight: 400;
  }
</style>
</head>
<body>
<main class="canvas">

  <section class="card card--front" aria-label="Business card front">
    <div class="ghost-circle"></div>
    <div class="brand">
      <span class="brand__mark"></span>
      <span class="brand__name">Meridel Capra</span>
    </div>
    <p class="website">www.meridelcapra.ch</p>
  </section>

  <section class="card card--back" aria-label="Business card back">
    <div class="brand">
      <span class="brand__mark"></span>
      <span class="brand__name">Meridel Capra</span>
    </div>

    <div class="holder">
      <h1 class="holder__name"><span class="holder__first">Paulo</span> <span class="holder__last">Vestrand</span></h1>
      <ul class="contact-list">
        <li>022 555 01 48
          <svg viewBox="0 0 24 24" aria-hidden="true"><path d="M6.6 10.8a15.1 15.1 0 0 0 6.6 6.6l2.2-2.2a1 1 0 0 1 1-.25 11.4 11.4 0 0 0 3.6.57 1 1 0 0 1 1 1V20a1 1 0 0 1-1 1A17 17 0 0 1 3 4a1 1 0 0 1 1-1h3.5a1 1 0 0 1 1 1c0 1.25.2 2.45.57 3.57a1 1 0 0 1-.25 1z"/></svg>
        </li>
        <li>paulo@meridelcapra.com
          <svg viewBox="0 0 24 24" aria-hidden="true"><path d="M2 5h20v14H2z M3.5 6.5 12 12.5l8.5-6" fill="var(--accent)"/><path d="M3 6l9 6.5L21 6" fill="none" stroke="#3f4d5f" stroke-width="1.5"/></svg>
        </li>
        <li>www.meridelcapra.ch
          <svg viewBox="0 0 24 24" aria-hidden="true"><circle cx="12" cy="12" r="9.5" fill="none" stroke="var(--accent)" stroke-width="2"/><ellipse cx="12" cy="12" rx="4" ry="9.5" fill="none" stroke="var(--accent)" stroke-width="1.6"/><path d="M2.5 12h19M4 7h16M4 17h16" stroke="var(--accent)" stroke-width="1.5"/></svg>
        </li>
      </ul>
    </div>

    <div class="rule"></div>

    <address class="address">
      Chemin des Orvets 17<br>
      1226 Thônex<br>
      Switzerland
    </address>
  </section>

</main>
</body>
</html>
```